Criação de Papelaria Profissional para Consultoria de Negócios
A empresa queria:
" Serviços de Consultoria de Carreira (transição, desenvolvimento de liderança), Assessment, Coaching, Outplacement, Headhunting "

```html
<!DOCTYPE html>
<html lang="pt-BR">
<head>
<meta charset="UTF-8">
<title>Lívia Montari – Consultoria de Carreira</title>
<link rel="stylesheet" href="https://fonts.googleapis.com/css2?family=Cinzel:wght@400;500&family=Montserrat:wght@400;500&display=swap">
<style>
  :root{
    --bg:#ebe8e5;
    --wine:#6e1419;
    --wine-dark:#3d080b;
    --wine-light:#8e2128;
    --paper:#ffffff;
    --ink:#5a5a5a;
    --ink-soft:#9a9a9a;
    --cream:#f4eeee;
  }
  *{margin:0;padding:0;box-sizing:border-box}
  html,body{width:1200px;height:1200px;overflow:hidden;background:var(--bg)}
  .canvas{width:1200px;height:1200px;display:flex;flex-direction:column;align-items:center;justify-content:center;gap:70px}
  .card{width:900px;height:514px;border-radius:40px;position:relative;overflow:hidden;box-shadow:0 10px 30px rgba(0,0,0,.12)}

  /* back: contact side */
  .card--back{background:var(--paper)}
  .card--back .identity{position:absolute;left:70px;top:70px}
  .identity__name{font-family:"Cinzel",serif;font-size:40px;color:var(--wine);letter-spacing:.04em;line-height:1}
  .identity__role{font-family:"Cinzel",serif;font-size:13px;color:var(--ink-soft);letter-spacing:.32em;margin-top:8px}
  .contacts{position:absolute;left:70px;top:200px;list-style:none;display:flex;flex-direction:column;gap:26px}
  .contact{display:flex;align-items:center;gap:18px;font-family:"Montserrat",sans-serif;font-size:16px;color:var(--ink);line-height:1.45}
  .contact__icon{width:34px;height:34px;border-radius:50%;background:var(--wine);flex:none;display:flex;align-items:center;justify-content:center}
  .contact__icon svg{width:18px;height:18px}
  .brand-mark{position:absolute;right:80px;top:50%;transform:translateY(-50%);display:flex;flex-direction:column;align-items:center;gap:18px}
  .brand-mark__halo{position:absolute;right:-120px;top:50%;transform:translateY(-50%);width:460px;height:460px;border-radius:50%;background:var(--cream)}
  .brand-mark__dot{width:22px;height:22px;border-radius:50%;background:var(--wine);position:relative}
  .brand-mark__name{font-family:"Cinzel",serif;font-size:34px;color:var(--wine);letter-spacing:.04em;position:relative}

  /* front: brand side */
  .card--front{background:radial-gradient(ellipse at 50% 40%,var(--wine-light) 0%,var(--wine) 45%,var(--wine-dark) 100%);display:flex;flex-direction:column;align-items:center;justify-content:center}
  .front__dot{width:26px;height:26px;border-radius:50%;background:rgba(255,255,255,.85);margin-bottom:34px}
  .front__name{font-family:"Cinzel",serif;font-size:70px;color:#fff;letter-spacing:.06em;line-height:1}
  .front__rule{width:470px;height:1px;background:rgba(255,255,255,.6);margin:14px 0 10px}
  .front__role{font-family:"Cinzel",serif;font-size:22px;color:rgba(255,255,255,.9);letter-spacing:.34em}
</style>
</head>
<body>
<main class="canvas">
  <section class="card card--back" aria-label="Verso do cartão com contatos">
    <div class="brand-mark__halo"></div>
    <header class="identity">
      <h1 class="identity__name">LÍVIA MONTARI</h1>
      <p class="identity__role">CONSULTORIA DE CARREIRA</p>
    </header>
    <ul class="contacts">
      <li class="contact">
        <span class="contact__icon"><svg viewBox="0 0 24 24" fill="#fff"><path d="M6.6 10.8a15.1 15.1 0 0 0 6.6 6.6l2.2-2.2a1 1 0 0 1 1-.25 11.4 11.4 0 0 0 3.6.57 1 1 0 0 1 1 1V20a1 1 0 0 1-1 1A17 17 0 0 1 3 4a1 1 0 0 1 1-1h3.5a1 1 0 0 1 1 1c0 1.25.2 2.45.57 3.57a1 1 0 0 1-.25 1z"/></svg></span>
        <span>(11) 5550-0142<br>(11) 95550-0187</span>
      </li>
      <li class="contact">
        <span class="contact__icon"><svg viewBox="0 0 24 24" fill="none" stroke="#fff" stroke-width="2"><rect x="3" y="5" width="18" height="14" rx="2"/><path d="M3 7l9 6 9-6"/></svg></span>
        <span>contato@liviamontari.com.br<br>www.liviamontari.com.br</span>
      </li>
      <li class="contact">
        <span class="contact__icon"><svg viewBox="0 0 24 24" fill="#fff"><path d="M12 2a7 7 0 0 0-7 7c0 5.2 7 13 7 13s7-7.8 7-13a7 7 0 0 0-7-7zm0 9.5A2.5 2.5 0 1 1 12 6.5a2.5 2.5 0 0 1 0 5z"/></svg></span>
        <span>Rua das Acácias, 240 – Sala 12<br>Centro – São Paulo – SP</span>
      </li>
    </ul>
    <div class="brand-mark">
      <span class="brand-mark__dot"></span>
      <span class="brand-mark__name">Lívia Montari</span>
    </div>
  </section>

  <section class="card card--front" aria-label="Frente do cartão">
    <span class="front__dot"></span>
    <h2 class="front__name">LÍVIA MONTARI</h2>
    <span class="front__rule"></span>
    <p class="front__role">CONSULTORIA DE CARREIRA</p>
  </section>
</main>
</body>
</html>
```